Letterhead and Envelope Only (no biz card)
Leadership Development & Coaching Start Up
I also really like it when the swirls are not perfectly positioned on the page...bleeding off the page looks good. Thanks everyone!
Thanks for submitting your designs! Something else to keep in mind, I am rather feminine...I prefer softer lines and fainter watermarks in the background. I also really prefer the contact info to be on the bottom of the design.
Correction, I like the contact info on the bottom in #1 (not #3.)
My logo designer is out of the country, I should have those files for you in the next couple of days.
From the three designs so far, I like the swirls in #2. I like the contact info on the bottom in #3.
If possible, I'd like to have 2 letterhead designs in my winner...so I can use both for various purposes.
could you please upload the ai or eps file of logo?

```html
<!DOCTYPE html>
<html lang="en">
<head>
<meta charset="utf-8">
<title>Velmora Stationery – Envelope and Letterhead</title>
<link href="https://fonts.googleapis.com/css2?family=Nunito+Sans:wght@400;800&display=swap" rel="stylesheet">
<style>
  :root {
    --backdrop: #b4b4b6;
    --paper: #ffffff;
    --navy: #1c3f8f;
    --gold: #fdb913;
    --gold-deep: #f2a900;
    --blush: #fbe3c2;
    --ink: #3a3a3a;
    --window: #d9d9db;
  }
  * { box-sizing: border-box; margin: 0; padding: 0; }
  html, body { width: 1200px; height: 859px; overflow: hidden; }
  body {
    background: var(--backdrop);
    font-family: "Nunito Sans", sans-serif;
    position: relative;
  }
  .piece { position: absolute; overflow: hidden; }
  .piece > svg.shape { position: absolute; inset: 0; width: 100%; height: 100%; }

  .envelope-flap { position: absolute; left: 29px; top: 372px; width: 566px; height: 110px; }
  .envelope { left: 29px; top: 480px; width: 566px; height: 288px; }
  .letterhead { left: 619px; top: 43px; width: 550px; height: 725px; }

  .decor {
    position: absolute;
    border-radius: 50%;
    background: radial-gradient(circle, rgba(251,227,194,0.9) 0%, rgba(251,227,194,0.35) 60%, rgba(251,227,194,0) 72%);
  }

  .brand { position: absolute; }
  .brand-name {
    display: flex; align-items: center; gap: 8px;
    color: var(--navy); font-weight: 800; letter-spacing: -0.5px; line-height: 1;
  }
  .brand-dot { border-radius: 50%; background: var(--gold); display: inline-block; }
  .brand-tagline {
    background: var(--gold); color: var(--navy);
    font-weight: 400; text-transform: uppercase; letter-spacing: 1px;
    margin-top: 3px; padding: 1px 4px; white-space: nowrap;
  }
  .letterhead .brand { left: 22px; top: 30px; }
  .letterhead .brand-name { font-size: 40px; }
  .letterhead .brand-dot { width: 18px; height: 18px; }
  .letterhead .brand-tagline { font-size: 6px; width: 178px; }
  .envelope .brand { left: 40px; top: 38px; }
  .envelope .brand-name { font-size: 44px; }
  .envelope .brand-dot { width: 20px; height: 20px; }
  .envelope .brand-tagline { font-size: 6px; width: 196px; }

  .address-window {
    position: absolute; left: 43px; top: 127px; width: 272px; height: 89px;
    background: var(--window); border-radius: 8px;
  }
  .contact {
    position: absolute; color: var(--ink); font-size: 6.5px; line-height: 1.45;
  }
  .contact p + p.gap { margin-top: 4px; }
  .web { position: absolute; color: var(--ink); font-size: 6.5px; }
  .envelope .contact { left: 52px; top: 228px; }
  .envelope .web { right: 26px; bottom: 14px; }
  .letterhead .contact { left: 110px; top: 655px; }
  .letterhead .web { right: 20px; bottom: 16px; }
</style>
</head>
<body>

  <svg class="envelope-flap" viewBox="0 0 566 110" aria-hidden="true">
    <path d="M0,110 C80,70 230,6 343,2 C420,0 520,70 566,110 Z" fill="var(--gold)"/>
    <path d="M0,110 C80,70 230,6 343,2" fill="none" stroke="var(--gold-deep)" stroke-width="2"/>
  </svg>

  <section class="piece envelope" aria-label="Velmora envelope">
    <svg class="shape" viewBox="0 0 566 288" preserveAspectRatio="none" aria-hidden="true">
      <rect width="566" height="288" fill="var(--navy)"/>
      <rect x="300" width="266" height="120" fill="var(--gold)"/>
      <path d="M0,0 H460 C530,0 566,40 566,90 V288 H110 C50,288 0,250 0,160 Z" fill="var(--paper)"/>
    </svg>
    <div class="decor" role="img" aria-label="Faint peach swirl watermark" style="left:70px;top:10px;width:200px;height:200px;"></div>
    <div class="decor" role="img" aria-label="Faint peach palm leaf watermark" style="left:370px;top:8px;width:170px;height:150px;"></div>

    <div class="brand">
      <div class="brand-name">Velmora <span class="brand-dot"></span></div>
      <div class="brand-tagline">Leadership Coaching</div>
    </div>
    <div class="address-window"></div>
    <div class="contact">
      <p>48 Harbor Lane Suite 210</p>
      <p>Denver, CO 80202</p>
      <p class="gap">303.555.0142</p>
      <p>hello@velmoracoaching.com</p>
    </div>
    <div class="web">www.velmoracoaching.com</div>
  </section>

  <section class="piece letterhead" aria-label="Velmora letterhead">
    <svg class="shape" viewBox="0 0 550 725" preserveAspectRatio="none" aria-hidden="true">
      <rect width="550" height="725" fill="var(--navy)"/>
      <rect x="300" width="250" height="300" fill="var(--gold)"/>
      <path d="M0,0 H440 C505,0 550,60 550,140 V725 H110 C40,725 0,680 0,600 Z" fill="var(--paper)"/>
    </svg>
    <div class="decor" role="img" aria-label="Faint peach swirl watermark" style="left:40px;top:40px;width:280px;height:300px;"></div>
    <div class="decor" role="img" aria-label="Faint peach palm leaf watermark" style="left:340px;top:270px;width:220px;height:270px;"></div>
    <div class="decor" role="img" aria-label="Faint peach swirl watermark" style="left:340px;top:540px;width:200px;height:180px;"></div>

    <div class="brand">
      <div class="brand-name">Velmora <span class="brand-dot"></span></div>
      <div class="brand-tagline">Leadership Coaching</div>
    </div>
    <div class="contact">
      <p>48 Harbor Lane Suite 210</p>
      <p>Denver, CO 80202</p>
      <p class="gap">303.555.0142</p>
      <p>hello@velmoracoaching.com</p>
    </div>
    <div class="web">www.velmoracoaching.com</div>
  </section>

</body>
</html>
```